Threadpost Rancher Web Site

I've got great graphics, need a clean modern web site designed around them.

The Threadpost Rancher runs Email Discussion Groups, and needs an updated web site. The graphics are changing, the words are changing, the URL's will stay the same. The old site is www.grupo-relay.example

You can use Lorem Ipsum for the wording.

You can drop the video on the home page.

I may drop the About Us page.

The primary graphic is - https://trunk.x7vvbnre214kpz.hostvale.example/large_graphics/jpeg_png/threadpost-rancher/

I'd like to take a couple of the other horizontal graphics at - https://trunk.x7vvbnre214kpz.hostvale.example/large_graphics/jpeg_png/

And use them for parallax scrolling on the home page.

I've got a lot of cowboy gear graphics at - https://trunk.x7vvbnre214kpz.hostvale.example/misc_graphics/

That can be used as filler.

You need to figure out a color theme and fonts to use.

Good luck and have fun.

Doug
p.s Ask me for a zip file of the graphics on the above link.

Number of Pages Required

1 page

Requirements
Should not have
• No Stock Photos

```html
<!DOCTYPE html>
<html lang="en">
<head>
<meta charset="utf-8">
<title>Threadpost Rancher</title>
<link href="https://fonts.googleapis.com/css2?family=Lato:wght@300;400;700;900&display=swap" rel="stylesheet">
<style>
:root{
  --brown:#7a3a1c;
  --blue:#1f5e87;
  --blue-dark:#1d577d;
  --ink:#222;
  --muted:#666;
  --beige:#f8f5f0;
  --grey:#f0eeea;
  --white:#fff;
}
*{margin:0;padding:0;box-sizing:border-box}
html,body{width:1200px;height:4311px;overflow:hidden}
body{position:relative;font-family:"Lato",sans-serif;color:var(--ink);background:var(--white)}
.abs{position:absolute}
a{color:inherit;text-decoration:none}
.btn{position:absolute;display:flex;align-items:center;justify-content:center;background:var(--brown);color:#fff;font-weight:700;border-radius:2px}
.brand{display:flex;align-items:center;gap:10px;font-weight:900;font-size:15px;color:var(--ink)}
.brand-dot{width:36px;height:36px;border-radius:50%;background:var(--brown)}
.hero{left:0;top:0;width:1200px;height:636px;background:linear-gradient(180deg,#f6f3ee,#ece8e2)}
.nav{top:82px;left:0;width:1200px;display:flex;justify-content:center;gap:48px;font-size:12px;color:#333}
.nav .active{color:var(--brown)}
.hero-title{left:159px;top:238px;font-weight:400;font-size:38px;line-height:1.05;color:#1a1a1a}
.hero-title span{display:block;color:var(--blue);font-weight:700;font-size:44px}
.hero-text{left:159px;top:330px;width:430px;font-size:15px;line-height:21px;color:#444}
.call{left:159px;top:478px;font-size:14px;color:var(--blue);display:flex;gap:6px;align-items:center}
.call b{color:#222;font-weight:700}
.hero-art{left:686px;top:126px;width:402px;height:494px;border-radius:40% 30% 20% 20%;background:radial-gradient(ellipse at 50% 40%,#8b4a22,#5e2c14 60%,rgba(236,232,226,0) 72%)}
.tools-title{left:159px;top:690px;font-size:36px;line-height:38px;font-weight:700;color:var(--blue)}
.tools-text{left:159px;top:776px;width:360px;font-size:12px;line-height:19px;color:#333}
.feature{width:210px}
.feature svg{display:block;margin-bottom:8px}
.feature h3{font-size:18px;font-weight:700;color:var(--brown);margin-bottom:8px}
.feature p{font-size:12px;line-height:19px;color:#888}
.privacy{left:0;top:1068px;width:1200px;height:860px;background:var(--beige)}
.privacy-bottom{left:0;top:1360px;width:1200px;height:568px}
.video{left:159px;top:1133px;width:419px;height:245px;background:#fff;padding:9px;box-shadow:0 2px 10px rgba(0,0,0,.15)}
.video-fill{width:100%;height:100%;background:linear-gradient(160deg,#cfe3df,#b9a07a 55%,#6d5b3d)}
.play{left:343px;top:1230px;width:50px;height:50px;border-radius:50%;background:rgba(255,255,255,.8);display:flex;align-items:center;justify-content:center}
.privacy-title{left:608px;top:1186px;font-size:34px;line-height:41px;font-weight:700;color:var(--blue)}
.clients-title{left:0;width:1200px;top:1512px;text-align:center;font-size:34px;font-weight:700;color:var(--blue)}
.client-row{left:150px;width:900px;display:flex}
.client{flex:1;height:90px;display:flex;align-items:center;justify-content:center;gap:8px;font-size:14px;font-weight:700;color:#555;border-right:1px solid #e2dfda;text-align:center;padding:0 6px}
.client:last-child{border-right:0}
.client i{width:14px;height:14px;border-radius:50%;background:#9a9a9a;flex:none}
.dots{left:580px;top:1872px;display:flex;gap:8px}
.dots span{width:8px;height:8px;border-radius:50%;background:#ccc}
.dots span:first-child{background:none;border:1px solid var(--blue)}
.diff{left:367px;top:1928px;width:833px;height:499px;background:var(--blue)}
.diff-title{left:434px;top:1986px;font-size:36px;font-weight:700;color:#fff}
.stat{width:290px;color:#fff}
.stat h4{font-size:20px;font-weight:900}
.stat h5{font-size:17px;font-weight:400;color:#cfe0ec;padding-bottom:8px;border-bottom:2px solid #fff;display:inline-block;margin-bottom:12px}
.stat p{font-size:12px;line-height:18px;color:#dbe6ee}
.cust-panel{left:0;top:2427px;width:1041px;height:461px;background:var(--beige)}
.cust-title{left:159px;top:2506px;font-size:36px;line-height:42px;font-weight:700;color:var(--blue)}
.arrow-btn{left:484px;top:2520px;width:62px;height:62px;border-radius:50%;border:2px solid var(--brown);display:flex;align-items:center;justify-content:center}
.quote-mark{left:159px;top:2614px;font-size:40px;font-weight:900;color:#333;line-height:1}
.quote{left:156px;top:2648px;width:360px;font-size:17px;line-height:26px;color:#333}
.quote-name{left:159px;top:2740px;font-size:18px;color:var(--brown)}
.quote-role{left:159px;top:2764px;font-size:12px;color:#888}
.cust-photo{left:561px;top:2440px;width:443px;height:448px;border-radius:50% 50% 20px 20px / 45% 45% 20px 20px;background:linear-gradient(180deg,#6b4a36,#8a8b8c 45%,#5c5f63)}
.blog-title{left:0;width:1200px;top:2936px;text-align:center;font-size:34px;font-weight:700;color:var(--blue)}
.blog-bg{left:92px;top:3080px;width:1108px;height:499px;background:#f3f3f3}
.blog-side{left:0;top:3251px;width:92px;height:328px;background:var(--blue)}
.card{width:435px;height:432px;background:#fff;box-shadow:0 2px 8px rgba(0,0,0,.08)}
.card-img{height:232px}
.card-body{padding:18px 20px}
.card h3{font-size:18px;font-weight:400;color:var(--blue)}
.card time{font-size:12px;color:#999;display:block;margin:2px 0 16px}
.card p{font-size:12px;line-height:19px;color:#888}
.card .more{display:block;margin-top:14px;font-size:15px;color:var(--blue)}
.cta{left:0;top:3579px;width:1200px;height:350px;background:var(--blue-dark);color:#fff;text-align:center}
.cta h2{position:absolute;top:102px;width:100%;font-size:35px;font-weight:700}
.cta p{position:absolute;top:156px;width:100%;font-size:18px;color:#e3edf4}
.cta-btn{position:absolute;left:499px;top:197px;width:202px;height:42px;background:#fff;color:var(--blue);font-weight:700;font-size:15px;display:flex;align-items:center;justify-content:center}
.foot-text{left:159px;top:4046px;width:280px;font-size:13px;line-height:20px;color:#555}
.socials{left:159px;top:4163px;display:flex;gap:10px}
.socials span{width:30px;height:30px;border-radius:50%;border:2px solid var(--blue)}
.foot-col h4{font-size:18px;font-weight:400;color:var(--brown);margin-bottom:20px}
.foot-col li{list-style:none;font-size:13px;color:#555;line-height:28px}
.copy{left:0;width:1200px;top:4271px;text-align:center;font-size:12px;color:#555}
</style>
</head>
<body>

<section class="abs hero"></section>
<div class="abs brand" style="left:159px;top:14px"><span class="brand-dot"></span>Threadpost Rancher</div>
<div class="abs" style="left:744px;top:29px;font-size:12px;color:#333">English ▾</div>
<div class="abs" style="left:834px;top:18px;display:flex;align-items:center;gap:8px;font-size:13px;color:var(--brown)">
  <svg width="34" height="34" viewBox="0 0 34 34"><circle cx="17" cy="17" r="15.5" fill="none" stroke="#333" stroke-width="2"/><circle cx="17" cy="13" r="4" fill="#333"/><path d="M10 24c1-4 4-6 7-6s6 2 7 6z" fill="#333"/></svg>Log In</div>
<a class="btn" style="left:922px;top:14px;width:121px;height:42px;font-size:13px">Sign Up Free</a>
<nav class="abs nav"><a class="active">Home</a><a>Why Rancher</a><a>Pricing</a><a>Features</a><a>Blog</a><a>Contact</a></nav>

<h1 class="abs hero-title">Fast delivery for your<span>application emails</span></h1>
<p class="abs hero-text">Many desktop publishing packages and web page editors now use Lorem Ipsum as their default model text, and a search for 'lorem ipsum' will uncover many web sites still in their infancy.</p>
<a class="btn" style="left:159px;top:424px;width:204px;height:45px;font-size:15px">Start a free trial</a>
<div class="abs call"><svg width="16" height="16" viewBox="0 0 16 16"><path d="M3 1l3 3-2 2c1 2 3 4 5 5l2-2 3 3-2 2C7 14 2 9 1 3z" fill="#1f5e87"/></svg>Call us at <b>1-800-555-0142</b></div>
<div class="abs hero-art" role="img" aria-label="Illustration of a cowboy on a rearing horse"></div>

<h2 class="abs tools-title">All the tools<br>you need...</h2>
<p class="abs tools-text">It is a long established fact that a reader will be distracted by the readable content of a page when looking at its layout. The point of using Lorem Ipsum is that it has a more-or-less normal distribution of letters, as opposed to using 'Content here, content here', making it look like readable English.</p>
<div class="abs feature" style="left:593px;top:692px"><svg width="24" height="20" viewBox="0 0 24 20"><rect x="2" y="4" width="20" height="13" fill="none" stroke="#7a3a1c" stroke-width="1.5"/><path d="M2 4l10 8 10-8" fill="none" stroke="#7a3a1c" stroke-width="1.5"/></svg><h3>Email Marketing</h3><p>It is a long established fact that a reader will be distracted by the readable content of a page when looking at its layout.</p></div>
<div class="abs feature" style="left:842px;top:692px"><svg width="24" height="20" viewBox="0 0 24 20"><rect x="3" y="3" width="18" height="12" rx="2" fill="none" stroke="#7a3a1c" stroke-width="1.5"/><path d="M7 15l-2 4 6-4" fill="none" stroke="#7a3a1c" stroke-width="1.5"/></svg><h3>Sms Marketing</h3><p>It is a long established fact that a reader will be distracted by the readable content of a page when looking at its layout.</p></div>
<div class="abs feature" style="left:593px;top:866px"><svg width="30" height="24" viewBox="0 0 30 24"><ellipse cx="17" cy="9" rx="11" ry="7" fill="none" stroke="#7a3a1c" stroke-width="1.5"/><ellipse cx="10" cy="15" rx="8" ry="5" fill="#fff" stroke="#7a3a1c" stroke-width="1.5"/></svg><h3>Chat</h3><p>It is a long established fact that a reader will be distracted by the readable content of a page when looking at its layout.</p></div>
<div class="abs feature" style="left:842px;top:866px"><svg width="24" height="24" viewBox="0 0 24 24"><rect x="4" y="2" width="16" height="20" fill="none" stroke="#7a3a1c" stroke-width="1.5"/><path d="M8 8h8M8 12h8M8 16h6" stroke="#7a3a1c" stroke-width="1.5"/></svg><h3>Any Size File</h3><p>It is a long established fact that a reader will be distracted by the readable content of a page when looking at its layout.</p></div>

<section class="abs privacy"></section>
<svg class="abs privacy-bottom" width="1200" height="568" viewBox="0 0 1200 568"><polygon points="0,120 1200,0 1200,568 0,568" fill="#f0eeea"/></svg>
<div class="abs video"><div class="video-fill" role="img" aria-label="Illustration of a stagecoach pulled by horses in the desert"></div></div>
<div class="abs play"><svg width="20" height="20" viewBox="0 0 20 20"><path d="M6 3l11 7-11 7z" fill="#7a3a1c"/></svg></div>
<h2 class="abs privacy-title">Your data privacy<br>and security are a top<br>concern for us.</h2>

<h2 class="abs clients-title">Selected Clients</h2>
<div class="abs client-row" style="top:1596px">
  <div class="client"><i></i>Abrelle Living</div><div class="client"><i></i>Hollenway Care</div><div class="client"><i></i>Westvale Hospital Guild</div><div class="client"><i></i>Northbay Dental Circle</div><div class="client">Quenlix</div>
</div>
<div class="abs client-row" style="top:1744px">
  <div class="client"><i></i>Harbor School Nurses</div><div class="client"><i></i>Tavisford Institute</div><div class="client">Pemberly Fund</div><div class="client">Tonewell Makers Group</div><div class="client"><i></i>Ridgefold Council</div>
</div>
<div class="abs dots"><span></span><span></span><span></span></div>

<section class="abs diff"></section>
<h2 class="abs diff-title">Whats Different</h2>
<div class="abs stat" style="left:438px;top:2066px"><h4>100 MILLION</h4><h5>emails every day</h5><p>There are many variations of passages of Lorem Ipsum available, but the majority have suffered alteration . .</p></div>
<div class="abs stat" style="left:755px;top:2066px"><h4>10 YEARS</h4><h5>expertise</h5><p>There are many variations of passages of Lorem Ipsum available, but the majority have suffered alteration . .</p></div>
<div class="abs stat" style="left:438px;top:2232px"><h4>80 THOUSAND</h4><h5>users in 160 countries</h5><p>There are many variations of passages of Lorem Ipsum available, but the majority have suffered alteration . .</p></div>
<div class="abs stat" style="left:755px;top:2232px"><h4>$0</h4><h5>to get started</h5><p>There are many variations of passages of Lorem Ipsum available, but the majority have suffered alteration . .</p></div>

<section class="abs cust-panel"></section>
<h2 class="abs cust-title">Our customers<br>love us!</h2>
<div class="abs arrow-btn"><svg width="26" height="16" viewBox="0 0 26 16"><path d="M1 8h23M17 1l7 7-7 7" fill="none" stroke="#7a3a1c" stroke-width="2"/></svg></div>
<div class="abs quote-mark">“</div>
<p class="abs quote">It is a long established fact that a reader will be distracted by the readable content of a page when looking at its layout.</p>
<div class="abs quote-name">Marla Quint</div>
<div class="abs quote-role">Founder Of Lorem Ipsum</div>
<div class="abs cust-photo" role="img" aria-label="Photo of a smiling customer on the phone holding a tablet"></div>

<h2 class="abs blog-title">Blog Post</h2>
<div class="abs blog-bg"></div>
<div class="abs blog-side"></div>
<article class="abs card" style="left:159px;top:3021px"><div class="card-img" role="img" aria-label="Illustration of a stagecoach in the desert" style="background:linear-gradient(160deg,#cfe3df,#b49a72 55%,#6a5a3c)"></div><div class="card-body"><h3>Rowan Hale</h3><time>February 12, 2018</time><p>It is a long established fact that a reader will be distracted by the readable content of a page when looking at its layout. The point of using Lorem Ipsum . . .</p><a class="more">Read More</a></div></article>
<article class="abs card" style="left:633px;top:3021px"><div class="card-img" role="img" aria-label="Illustration of a cowboy with a lasso on horseback" style="background:linear-gradient(160deg,#e0b772,#b6773a 55%,#6e4322)"></div><div class="card-body"><h3>Rowan Hale</h3><time>February 12, 2018</time><p>It is a long established fact that a reader will be distracted by the readable content of a page when looking at its layout. The point of using Lorem Ipsum . . .</p><a class="more">Read More</a></div></article>
<a class="btn" style="left:499px;top:3485px;width:202px;height:42px;font-size:14px">View All Post</a>

<section class="abs cta"><h2>Ready to get started?</h2><p>Join thousands of businesses that already trust their email delivery to Mailstead.</p><a class="cta-btn">Start Free Trial</a></section>

<div class="abs brand" style="left:159px;top:3972px"><span class="brand-dot"></span>Threadpost Rancher</div>
<p class="abs foot-text">Contrary to popular belief, Lorem Ipsum is not simply random text. It has roots in a piece of classical Latin literature from 45 BC, making it over 2000 years old. Edwin Farrow, a Latin professor at</p>
<div class="abs socials" role="img" aria-label="Social network links"><span></span><span></span><span></span><span></span></div>
<div class="abs foot-col" style="left:534px;top:3980px"><h4>Quick Link</h4><ul><li>Home</li><li>Why Rancher</li><li>Pricing</li><li>Features</li><li>Blog</li><li>Contact</li></ul></div>
<div class="abs foot-col" style="left:735px;top:3980px"><h4>Solutions</h4><ul><li>Features</li><li>Enterprise offer</li><li>White Label &amp; Resellers</li><li>Postwren vs. Letterhop</li><li>Affiliate program</li><li>Lorem Ipsum</li></ul></div>
<div class="abs foot-col" style="left:962px;top:3980px"><h4>Get Help</h4><ul><li>Help</li><li>Contact</li><li>Schedule</li><li>Lorem Ipsum</li><li>Lorem Ipsum</li></ul></div>
<div class="abs copy">Copyright©2020 Threadpost Rancher , All Rights Reserved.</div>

</body>
</html>
```